Website Redesign for NeedleForge.co.za – Bold, Modern & Professional Tattoo Supply Store (B2B ...

PLEASE DO NOT CONTACT US OUTSIDE PIXELBAZAAR.COM

We’re looking for a skilled and creative web designer to redesign NeedleForge.co.za, a leading tattoo equipment and supplies store based in South Africa. The business serves both B2B (tattoo studios, artists, wholesalers) and B2C (individual customers) markets.

The current website is outdated and lacks the modern, edgy look that reflects the tattoo industry. We want a fresh, bold, and professional design that appeals to both professional artists and retail customers — combining trust, style, and functionality.

About the Business:
Needle Forge supplies a wide range of tattoo-related products, including machines, needles, inks, hygiene supplies, and accessories. The company is well-established in the South African market and serves both individual tattoo artists and studios, as well as end customers looking for quality equipment.

The website must reflect the creative, bold, and artistic nature of the tattoo industry, while still being easy to navigate, fast, and conversion-focused.

What We’re Looking For:
A bold, modern design with a clear structure
Strong visual identity that reflects the tattoo culture — edgy, artistic, but still clean and professional
A layout that works for both B2B and B2C audiences
Clear product presentation and strong CTAs (Buy Now, Request Quote, Contact, etc.)
Fully responsive design (desktop + mobile)
Easy-to-navigate product categories and filters
Space for featured products, promotions, and artist-focused content
Integration of trust elements (payment icons, reviews, certifications, etc.)

Pages We Need Designed:
Homepage
Product detail page

Inspiration / Style Direction:
We’re looking for something with a strong personality, inspired by tattoo culture, but still clean and user-friendly. Think:

Dark theme with bold highlights (but open to light themes if well executed)
High-quality visuals and product imagery

Examples for inspiration:
GrimQuill.co.uk
Marlow QRV
Corvane Needle Supply
Moxie Salve

Deliverables:
Full desktop and mobile designs (Figma, XD, or PSD)
All design source files
Fonts, icons, and assets used
Clearly labeled layers and organized files
Ready for development handoff

Target Market(s)

NeedleForge.co.za targets both B2B and B2C customers in South Africa: B2B: Professional tattoo artists, studios, and wholesalers looking for high-quality, reliable equipment and bulk pricing. B2C: Individual customers, hobbyists, and beginners seeking safe, affordable tattoo supplies with guidance and support. The site should appeal to both experienced professionals and newcomers, combining a bold, authentic tattoo vibe with a clean, user-friendly shopping experience.

Industry/Entity Type

Tattoo Equipment & Supplies – E-commerce (B2B & B2C)

Number of Pages Required

2 page

Requirements
Must have
• Responsive design, bold tattoo-inspired visual style, clear navigation for B2B & B2C, strong product presentation, clear call-to-actions, trust elements (reviews, badges, payment icons), category filters & search, dedicated B2B/wholesale info page, speed-optimized layout, easy access to contact & support.
Should not have
• Overly complex animations, cluttered layout, generic stock images, too many fonts or colors, hidden navigation, auto-play videos or sounds, outdated visual styles, low-quality product images, confusing checkout process, unnecessary pop-ups.

```html
<!DOCTYPE html>
<html lang="en">
<head>
<meta charset="utf-8">
<title>Needle Forge – Tattoo Supplies</title>
<link rel="stylesheet" href="https://fonts.googleapis.com/css2?family=Cinzel:wght@700;900&family=Poppins:wght@400;500;600;700&display=swap">
<style>
:root{
  --stage:#e2e3e7;
  --night:#0b0d22;
  --navy:#1e2238;
  --orange:#f9a20a;
  --tan:#c79a5a;
  --white:#ffffff;
  --muted:#c9cbd6;
  --line:#4a4f6a;
}
*{box-sizing:border-box;margin:0;padding:0}
html,body{width:1200px;height:3460px;overflow:hidden;background:var(--stage);font-family:"Poppins",sans-serif;color:var(--white)}
.page{position:absolute;left:114px;top:87px;width:972px;height:3286px;background:var(--night);box-shadow:4px 6px 14px rgba(0,0,0,.25);overflow:hidden}
.block{position:absolute;left:0;width:972px}
.inner{position:absolute;left:97px;width:778px}
.heading{font-family:"Cinzel",serif;font-weight:900;color:var(--orange);font-variant:small-caps;letter-spacing:1px}

/* top bar & header */
.topbar{top:0;height:29px;background:#151933;font-size:9px;z-index:2}
.topbar .follow{position:absolute;left:97px;top:9px;display:flex;gap:10px;align-items:center}
.dot-ico{width:10px;height:10px;border:1.3px solid var(--muted);border-radius:50%}
.topbar .phone{position:absolute;right:97px;top:8px;display:flex;gap:5px;align-items:center}
.hero{top:29px;height:448px;background:
  radial-gradient(ellipse 30% 40% at 50% 12%,#8a6a58 0%,transparent 70%),
  radial-gradient(ellipse 55% 45% at 70% 30%,#a06b4f 0%,#6b4535 45%,transparent 80%),
  radial-gradient(ellipse 60% 55% at 25% 70%,#b57a58 0%,#7a4c38 40%,transparent 75%),
  linear-gradient(160deg,#3a2a26 0%,#5a3a2c 40%,#2a1e1c 75%,#161420 100%)}
.hero-shade{position:absolute;inset:0;background:linear-gradient(180deg,rgba(10,12,30,.15),rgba(10,12,30,.35))}
.header{position:absolute;left:0;top:0;width:972px;height:92px;background:rgba(30,34,56,.78);z-index:2}
.logo{position:absolute;left:419px;top:-29px;width:136px;height:80px;background:var(--orange);display:flex;align-items:center;justify-content:center;font-weight:700;font-size:17px;letter-spacing:1px;color:var(--white)}
.search{position:absolute;left:97px;top:16px;width:235px;height:26px;border:1.3px solid var(--muted);border-radius:13px;font-size:8px;color:#8a8fa8;padding:6px 14px}
.search svg{position:absolute;right:8px;top:6px}
.tools{position:absolute;right:97px;top:14px;display:flex;gap:22px;align-items:center;font-size:8px}
.nav{position:absolute;left:97px;top:69px;width:778px;display:flex;justify-content:space-between;font-size:10px;font-weight:600}
.nav span:first-child{color:var(--orange)}
.hero-copy{position:absolute;left:0;top:196px;width:972px;text-align:center;z-index:1}
.hero-copy h1{font-size:36px;text-shadow:0 2px 8px rgba(0,0,0,.55);font-variant:normal;text-transform:uppercase}
.hero-copy p{font-size:15px;margin-top:12px;text-shadow:0 1px 4px rgba(0,0,0,.5)}
.cta{display:inline-flex;gap:10px;align-items:center;margin-top:22px;background:var(--orange);color:var(--white);font-size:10px;font-weight:600;padding:7px 16px;border-radius:14px}

/* trust strip */
.trust{top:477px;height:104px;background:var(--navy)}
.trust .inner{top:16px;display:flex;justify-content:space-between;align-items:center}
.trust-item{display:flex;gap:14px;align-items:center}
.ring{width:70px;height:70px;border:1.5px solid var(--muted);border-radius:50%;display:flex;align-items:center;justify-content:center}
.trust-item b{display:block;color:var(--orange);font-family:"Cinzel",serif;font-size:10px;font-variant:small-caps}
.trust-item span{font-size:10px}
.dash{width:45px;height:1px;background:var(--muted)}

/* categories */
.cats{top:581px;height:531px}
.cats h2{position:absolute;top:88px;width:972px;text-align:center;font-size:22px}
.cat{position:absolute;width:193px;height:110px;display:flex;align-items:center;gap:16px;font-size:11px;font-weight:500;border-bottom:1px solid var(--line)}
.cat.right{justify-content:flex-end}
.cat .thumb{width:84px;height:84px;border-radius:50%;border:2px solid #6a6f85;flex:0 0 84px}
.cat .arrow{margin-left:auto}
.cat.right .arrow{margin-left:0;margin-right:auto}
.t-ink{background:radial-gradient(circle at 45% 45%,#f2f2f2 0%,#8a8a90 30%,#1a1a1f 70%)}
.t-med{background:radial-gradient(circle at 50% 55%,#4caf62 0%,#2a6a3a 35%,#141a18 75%)}
.t-ndl{background:radial-gradient(circle at 50% 50%,#d9d9d9 0%,#3a3a40 30%,#0e0e12 70%)}
.t-fur{background:radial-gradient(circle at 50% 60%,#2a2420 0%,#6a5a48 45%,#b8a48a 100%)}
.t-acc{background:radial-gradient(circle at 50% 50%,#d94a3a 0%,#3a7fd0 40%,#e8c23a 70%,#1a1a22 100%)}
.t-con{background:radial-gradient(circle at 50% 50%,#8a7ac8 0%,#4a3a8a 45%,#1a1a3a 85%)}
.model{position:absolute;left:412px;top:145px;width:148px;height:386px;background:
  radial-gradient(ellipse 30% 12% at 50% 8%,#b07a5a 0%,transparent 100%),
  linear-gradient(180deg,#5a4038 0%,#8a6a5c 14%,#1a1a20 22%,#1a1a20 58%,#3a5a8c 62%,#4a6a9c 80%,#9a7664 88%,#7a5a4c 100%);border-radius:46px 46px 0 0}

/* product rows */
.rail{height:365px}
.rail h2{position:absolute;left:97px;top:28px;font-size:22px}
.pager{position:absolute;right:97px;top:38px;display:flex;gap:6px}
.pager i{width:16px;height:16px;border-radius:50%;background:#9a9cab}
.pager i:first-child{background:var(--orange)}
.cards{position:absolute;left:97px;top:82px;display:flex;gap:24px}
.card{position:relative;width:176px;height:232px;background:var(--white);border-radius:4px;color:#222}
.card .img{position:absolute;left:12px;top:14px;width:130px;height:130px;border-radius:4px}
.card .ribbon{position:absolute;left:6px;top:6px;width:38px;height:38px;background:linear-gradient(135deg,#d9261c 50%,transparent 50%)}
.card .ribbon span{position:absolute;left:2px;top:10px;transform:rotate(-45deg);font-size:8px;color:#fff}
.card .side{position:absolute;right:8px;top:14px;display:flex;flex-direction:column;gap:5px}
.card .side i{width:12px;height:12px;border:1px solid #999;border-radius:50%}
.card .side i.gold{border-color:var(--orange);background:#fde3a8}
.card .name{position:absolute;left:7px;top:166px;width:118px;font-size:8px;font-weight:600;line-height:1.25}
.card .qty{position:absolute;right:8px;top:168px;font-size:8px;color:#666}
.card .buy{position:absolute;left:7px;bottom:12px;background:var(--tan);color:var(--white);font-size:6px;padding:3px 5px;border-radius:2px}
.card .price{position:absolute;right:8px;bottom:12px;font-size:9px;font-weight:600}
.dots{position:absolute;left:474px;top:336px;display:flex;gap:6px}
.dots i{width:5px;height:5px;border-radius:50%;background:#8a8fa8}
.dots i:first-child{background:var(--white)}
.latest{top:1112px;background:var(--navy)}
.best{top:1524px}
.featured{top:1932px}
.p-black{background:radial-gradient(ellipse 45% 50% at 50% 52%,#111 0%,#2a2a2e 55%,#fff 100%)}
.p-brown{background:radial-gradient(ellipse 45% 40% at 50% 55%,#6a4530 0%,#e8e4de 60%,#fff 100%)}
.p-kraft{background:radial-gradient(ellipse 48% 22% at 50% 55%,#c9a27a 0%,#e8d5bd 60%,#fff 100%)}
.p-red{background:radial-gradient(ellipse 48% 40% at 50% 50%,#b8202a 0%,#e9a0a4 55%,#fff 100%)}
.p-grip{background:radial-gradient(ellipse 45% 40% at 50% 50%,#222 0%,#9a9a9a 50%,#fff 100%)}
.p-blue{background:radial-gradient(ellipse 30% 45% at 55% 50%,#6aa8d8 0%,#c8e0f2 55%,#fff 100%)}
.p-night{background:linear-gradient(160deg,#fff 15%,#1a3a8a 25%,#2a5ab8 55%,#0e1e4a 80%,#fff 90%)}
.p-glove{background:radial-gradient(ellipse 35% 48% at 50% 50%,#0a0a0a 0%,#3a3a3a 55%,#fff 100%)}
.p-coil{background:radial-gradient(ellipse 45% 45% at 50% 55%,#5a1e22 0%,#4a5a48 40%,#cfcfcf 75%,#fff 100%)}
.p-box{background:radial-gradient(ellipse 45% 28% at 50% 55%,#111 0%,#555 55%,#fff 100%)}
.p-sticks{background:radial-gradient(ellipse 45% 45% at 50% 50%,#151515 0%,#6a6a6a 55%,#fff 100%)}
.p-pens{background:radial-gradient(ellipse 45% 40% at 50% 50%,#e2cf9a 0%,#f4ecd6 60%,#fff 100%)}

/* register */
.register{top:2390px;height:462px;background:var(--navy)}
.studio{position:absolute;left:97px;top:59px;width:367px;height:344px;border-radius:10px;background:
  radial-gradient(ellipse 35% 30% at 30% 55%,#c08a6a 0%,transparent 100%),
  radial-gradient(ellipse 30% 35% at 75% 45%,#9a6a52 0%,transparent 100%),
  radial-gradient(ellipse 40% 40% at 85% 10%,#7ab0e0 0%,transparent 100%),
  linear-gradient(135deg,#6a6a6a 0%,#3a3a3e 40%,#1a1a1e 70%,#2a3a4a 100%)}
.form{position:absolute;left:414px;top:43px;width:463px;height:376px;background:var(--night);border-radius:12px;padding:16px 22px 0 86px;font-size:8px;font-weight:600}
.row{display:flex;gap:14px;margin-bottom:10px}
.field{flex:1}
.field label{display:block;margin-bottom:6px}
.field div{height:20px;border:1px solid var(--muted);font-weight:400;font-size:8px;padding:4px 3px}
.field.half{flex:0 0 169px}
.submit{width:169px;height:20px;background:var(--orange);text-align:center;line-height:20px;font-size:8px;margin-top:4px}

/* footer */
.footer{top:2852px;height:434px}
.f-logo{position:absolute;left:97px;top:110px;font-weight:700;font-size:26px;letter-spacing:1px}
.call{position:absolute;left:0;top:92px;width:972px;text-align:center}
.call b{display:block;color:var(--orange);font-weight:500;font-size:26px}
.call strong{display:block;font-size:28px;font-weight:600;margin-top:2px}
.social{position:absolute;right:97px;top:122px;display:flex;gap:20px}
.social i{width:26px;height:26px;border:1.8px solid var(--white);border-radius:50%}
.rule{position:absolute;left:97px;top:188px;width:778px;height:1px;background:var(--line)}
.rule.low{top:376px}
.col{position:absolute;top:218px;font-size:10.5px}
.col h4{font-family:"Cinzel",serif;font-variant:small-caps;color:var(--orange);font-size:12px;margin-bottom:14px}
.col p{margin-bottom:13px}
.copy{position:absolute;left:97px;top:398px;font-size:8.5px}
.pay{position:absolute;right:97px;top:392px;display:flex;gap:7px;align-items:center}
.pay .brand{font-size:16px;color:#9a9cab;margin-right:14px}
.pay i{width:34px;height:22px;border-radius:3px;background:#5a6fa8}
</style>
</head>
<body>
<div class="page">

  <div class="block topbar">
    <div class="follow">Follow Us: <i class="dot-ico"></i><i class="dot-ico"></i><i class="dot-ico"></i><i class="dot-ico"></i></div>
    <div class="phone">
      <svg width="10" height="10" viewBox="0 0 24 24"><path fill="#fff" d="M6.6 10.8a15 15 0 006.6 6.6l2.2-2.2a1 1 0 011-.25 11.4 11.4 0 003.6.57 1 1 0 011 1V20a1 1 0 01-1 1A17 17 0 013 4a1 1 0 011-1h3.5a1 1 0 011 1c0 1.25.2 2.45.57 3.57a1 1 0 01-.25 1z"/></svg>
      0825550193
    </div>
  </div>

  <section class="block hero" role="img" aria-label="Photo of an artist tattooing a client's back with gloved hands">
    <div class="hero-shade"></div>
    <div class="header">
      <div class="logo">NEEDLE FORGE</div>
      <div class="search">Search products
        <svg width="12" height="12" viewBox="0 0 24 24" fill="none" stroke="#fff" stroke-width="2"><circle cx="10" cy="10" r="7"/><path d="M15 15l6 6"/></svg>
      </div>
      <div class="tools">
        <svg width="20" height="18" viewBox="0 0 24 22" fill="none" stroke="#fff" stroke-width="1.6"><path d="M12 20S3 14 3 8a4.5 4.5 0 019-1 4.5 4.5 0 019 1c0 6-9 12-9 12z"/></svg>
        <span style="display:flex;gap:6px;align-items:center"><svg width="18" height="20" viewBox="0 0 24 24" fill="none" stroke="#fff" stroke-width="1.6"><circle cx="12" cy="8" r="4"/><path d="M4 21a8 8 0 0116 0"/></svg><span style="color:#4a72ff">Account</span></span>
        <span style="display:flex;gap:8px;align-items:center"><svg width="22" height="20" viewBox="0 0 24 24" fill="none" stroke="#fff" stroke-width="1.6"><path d="M3 4h3l2 12h11l2-8H7"/><circle cx="9" cy="20" r="1.4"/><circle cx="18" cy="20" r="1.4"/></svg><span>My Cart<br>$0.00</span></span>
      </div>
      <nav class="nav"><span>SpecialTattoo Ink ⌄</span><span>Medical Supplies ⌄</span><span>Needles ⌄</span><span>Furniture ⌄</span><span>Accessories ⌄</span><span>Consumables ⌄</span><span>Machines ⌄</span><span>Piercing ⌄</span><span>Expired Products ⌄</span><span>Blog</span></nav>
    </div>
    <div class="hero-copy">
      <h1 class="heading">Not a Tattoo Artist?</h1>
      <p>Visit our public retail store for non-regulated products.</p>
      <span class="cta">Go To Public Store <svg width="22" height="8" viewBox="0 0 22 8"><path d="M0 4h20M16 1l4 3-4 3" stroke="#fff" fill="none"/></svg></span>
    </div>
  </section>

  <section class="block trust">
    <div class="inner">
      <div class="trust-item"><div class="ring"><svg width="34" height="34" viewBox="0 0 24 24" fill="none" stroke="var(--orange)" stroke-width="1.3"><path d="M12 2l8 3v6c0 5-3.5 9-8 11-4.5-2-8-6-8-11V5z"/><circle cx="14" cy="14" r="4"/></svg></div><div><b>Secure Payments</b><span>Our website uses SSL</span></div></div>
      <div class="dash"></div>
      <div class="trust-item"><div class="ring"><svg width="36" height="30" viewBox="0 0 28 20" fill="none" stroke="var(--orange)" stroke-width="1.2"><rect x="3" y="3" width="15" height="11"/><path d="M18 7h5l3 4v3h-8"/><circle cx="8" cy="16" r="2"/><circle cx="21" cy="16" r="2"/></svg></div><div><b>Fast Shipping</b><span>We ship the same day</span></div></div>
      <div class="dash"></div>
      <div class="trust-item"><div class="ring"><svg width="34" height="34" viewBox="0 0 24 24" fill="none" stroke="var(--orange)" stroke-width="1.3"><path d="M12 2l9 5v10l-9 5-9-5V7z"/><path d="M3 7l9 5 9-5M12 12v10"/></svg></div><div><b>Extensive Stock Range</b><span>All products in stock</span></div></div>
    </div>
  </section>

  <section class="block cats">
    <h2 class="heading">Our Category</h2>
    <div class="cat" style="left:97px;top:130px"><div class="thumb t-ink" role="img" aria-label="Ink bottles"></div>Special<br>Tattoo Ink<svg class="arrow" width="14" height="24" viewBox="0 0 14 24"><path d="M2 2l10 10L2 22" stroke="#fff" stroke-width="2" fill="none"/></svg></div>
    <div class="cat" style="left:97px;top:255px"><div class="thumb t-med" role="img" aria-label="Medical supply packs"></div>Medical<br>Supplies<svg class="arrow" width="14" height="24" viewBox="0 0 14 24"><path d="M2 2l10 10L2 22" stroke="#fff" stroke-width="2" fill="none"/></svg></div>
    <div class="cat" style="left:97px;top:380px;border:0"><div class="thumb t-ndl" role="img" aria-label="Needle cartridge"></div>Needles<svg class="arrow" width="14" height="24" viewBox="0 0 14 24"><path d="M2 2l10 10L2 22" stroke="#fff" stroke-width="2" fill="none"/></svg></div>
    <div class="model" role="img" aria-label="Tattooed model in black top and denim shorts"></div>
    <div class="cat right" style="left:682px;top:130px"><svg class="arrow" width="14" height="24" viewBox="0 0 14 24"><path d="M12 2L2 12l10 10" stroke="#fff" stroke-width="2" fill="none"/></svg>Furniture<div class="thumb t-fur" role="img" aria-label="Tattoo studio bed"></div></div>
    <div class="cat right" style="left:682px;top:255px"><svg class="arrow" width="14" height="24" viewBox="0 0 14 24"><path d="M12 2L2 12l10 10" stroke="#fff" stroke-width="2" fill="none"/></svg>Accessories<div class="thumb t-acc" role="img" aria-label="Printed accessories"></div></div>
    <div class="cat right" style="left:682px;top:380px;border:0"><svg class="arrow" width="14" height="24" viewBox="0 0 14 24"><path d="M12 2L2 12l10 10" stroke="#fff" stroke-width="2" fill="none"/></svg>Consumables<div class="thumb t-con" role="img" aria-label="Consumable product artwork"></div></div>
  </section>

  <section class="block rail latest">
    <h2 class="heading">Latest Products</h2>
    <div class="pager"><i></i><i></i></div>
    <div class="cards">
      <div class="card"><div class="img p-black" role="img" aria-label="UV cabinet"></div><div class="ribbon"><span>New</span></div><div class="side"><i></i><i></i><i></i><i class="gold"></i></div><div class="name">UV Cabinet Large for Tattoo Tools</div><div class="qty">- 1 +</div><span class="buy">Buy Now</span><span class="price">$0.00</span></div>
      <div class="card"><div class="img p-brown" role="img" aria-label="Sterilising cabinet"></div><div class="ribbon"><span>New</span></div><div class="side"><i></i><i></i><i></i><i class="gold"></i></div><div class="name">UV Sterilising Cabinet for Tattoo Tools</div><div class="qty">- 1 +</div><span class="buy">Buy Now</span><span class="price">$0.00</span></div>
      <div class="card"><div class="img p-kraft" role="img" aria-label="Boxed pen machine sleeves"></div><div class="ribbon"><span>New</span></div><div class="side"><i></i><i></i><i></i><i class="gold"></i></div><div class="name">Elite Compostable Pen Machine Sleeves – 45 mm &amp; 55 mm (100 pcs)</div><div class="qty">- 1 +</div><span class="buy">Buy Now</span><span class="price">$0.00</span></div>
      <div class="card"><div class="img p-red" role="img" aria-label="Aftercare ointment sachets"></div><div class="ribbon"><span>New</span></div><div class="side"><i></i><i></i><i></i><i class="gold"></i></div><div class="name">Halvern Tattoo Aftercare Ointment</div><div class="qty">- 1 +</div><span class="buy">Buy Now</span><span class="price">$0.00</span></div>
    </div>
    <div class="dots"><i></i><i></i></div>
  </section>

  <section class="block rail best">
    <h2 class="heading" style="top:88px">Bestsellers</h2>
    <div class="pager" style="top:98px"><i></i><i></i></div>
    <div class="cards" style="top:142px">
      <div class="card"><div class="img p-grip" role="img" aria-label="Silica gel grips"></div><div class="side"><i></i><i></i><i></i><i class="gold"></i></div><div class="name">Disposable Silica Gel Grip 25mm (Price each) 20 pieces per box</div><div class="qty">- 1 +</div><span class="buy">Buy Now</span><span class="price">$0.00</span></div>
      <div class="card"><div class="img p-blue" role="img" aria-label="Liner cartridge"></div><div class="side"><i></i><i></i><i></i><i class="gold"></i></div><div class="name">Korvo Tattoo Liner Cartridges</div><div class="qty">- 1 +</div><span class="buy">Buy Now</span><span class="price">$0.00</span></div>
      <div class="card"><div class="img p-night" role="img" aria-label="Boxed ultra liners"></div><div class="side"><i></i><i></i><i></i></div><div class="name">Korvo Ultra Liners</div><div class="qty">- 1 +</div><span class="buy">Buy Now</span><span class="price">$0.00</span></div>
      <div class="card"><div class="img p-glove" role="img" aria-label="Black nitrile glove"></div><div class="side"><i></i><i></i><i></i><i class="gold"></i></div><div class="name">Silverpalm Black Nitrile Gloves</div><div class="qty">- 1 +</div><span class="buy">Buy Now</span><span class="price">$0.00</span></div>
    </div>
    <div class="dots" style="top:396px"><i></i><i></i></div>
  </section>

  <section class="block rail featured">
    <h2 class="heading" style="top:88px">Featured Products</h2>
    <div class="pager" style="top:98px"><i></i><i></i></div>
    <div class="cards" style="top:142px">
      <div class="card"><div class="img p-coil" role="img" aria-label="Coil tattoo machine"></div><div class="side"><i></i><i></i><i></i></div><div class="name">Redmond Burgundy Hound</div><div class="qty">- 1 +</div><span class="buy">Buy Now</span><span class="price">$0.00</span></div>
      <div class="card"><div class="img p-box" role="img" aria-label="Boxed liner cartridges"></div><div class="side"><i></i><i></i><i></i></div><div class="name">Korvo Tattoo Liner Cartridges</div><div class="qty">- 1 +</div><span class="buy">Buy Now</span><span class="price">$0.00</span></div>
      <div class="card"><div class="img p-sticks" role="img" aria-label="Ink mixer sticks"></div><div class="side"><i></i><i></i><i></i></div><div class="name">Pigment &amp; Ink Mixer Sticks 100</div><div class="qty">- 1 +</div><span class="buy">Buy Now</span><span class="price">$0.00</span></div>
      <div class="card"><div class="img p-pens" role="img" aria-label="Tattoo pen refills"></div><div class="side"><i></i><i></i><i></i></div><div class="name">Tattoo Pen Refills</div><div class="qty">- 1 +</div><span class="buy">Buy Now</span><span class="price">$0.00</span></div>
    </div>
    <div class="dots" style="top:396px"><i></i><i></i></div>
  </section>

  <section class="block register">
    <div class="studio" role="img" aria-label="Artist tattooing a smiling client in a studio"></div>
    <div class="form">
      <div class="row"><div class="field"><label>Email address</label><div>e.g jordan.vale@mail.com</div></div></div>
      <div class="row"><div class="field half"><label>First name</label><div></div></div><div class="field half"><label>Last name</label><div></div></div></div>
      <div class="row"><div class="field half"><label>Phone number</label><div></div></div></div>
      <div class="row"><div class="field"><label>Address</label><div></div></div></div>
      <div class="row"><div class="field half"><label>Suburb/town</label><div></div></div><div class="field half"><label>State/territory</label><div></div></div></div>
      <div class="row"><div class="field half"><label>Country</label><div></div></div><div class="field half"><label>Pincode</label><div></div></div></div>
      <div class="submit">Register Account</div>
    </div>
  </section>

  <footer class="block footer">
    <div class="f-logo">NEEDLE FORGE</div>
    <div class="call"><b>Call Us</b><strong>0825550193</strong></div>
    <div class="social"><i></i><i></i><i></i><i></i></div>
    <div class="rule"></div>
    <div class="col" style="left:97px"><h4>Information</h4><p>Track My Parcel</p><p>Delivery Information</p><p>About Us</p><p>Privacy Policy (POPI)</p></div>
    <div class="col" style="left:302px"><h4>&nbsp;</h4><p>Terms &amp; Conditions</p><p>Original Manufacturers</p><p>Guarantee</p><p>Cookies Policy</p></div>
    <div class="col" style="left:531px"><h4>Customer Service</h4><p>Contact Us</p><p>Returns</p><p>Site Map</p></div>
    <div class="col" style="left:785px"><h4>My Account</h4><p>Account</p><p>Order History</p><p>Wish List (0)</p><p>Newsletter</p></div>
    <div class="rule low"></div>
    <div class="copy">Copyright © 2025 NeedleForge Pty Ltd . All Rights Reserved.</div>
    <div class="pay"><span class="brand">kreditly</span><i></i><i style="background:#e08a2a"></i><i style="background:#2a4fb0"></i><i style="background:#f2f2f2"></i><i style="background:#c9472c"></i><i style="background:#3f7fd0"></i></div>
  </footer>

</div>
</body>
</html>
```